Graphics Design of Physics Book

Hi
Size : 8" x 11.25"
We are education book Publication Company and would like to have book cover for "Physics" it has 4 volumes. All 4 having the same color scheme and design except the volume no.
Blue is my personal favorite but u can use any color. Want to have a band at the bottom of the cover to place our Logo “VORLIN Education” a PDF of the same is attached, or you can place logo anywhere according to ur design.
I need “Physics” as title of the book to be visible prominently.
And volume and volume no. should also be Visible and eye catching I prefer a Graphic to enhance the Volume No.
A background pattern can also be a option (it should be vector form so that color can be change later)
Please do not offer any cut and paste design I need very professional presentation.
Volume and Number can be in metallic 3D (CMYK) effect.
only Professional presentation will get feedback.
I have provided a sample artwork for reference do not follow it but can be a reference what I needed !

Target Market(s)

Students Class 9th to 12th

Industry/Entity Type

Education

Font styles to use
Serif

Colors
3176b5
0555a3
85abd2
cadf82
abd036
9bcb3c

Requirements
Must have
• Eye catching.
• “Physics” as title of the book to be visible prominently.
• volume and volume no. should also be Visible and eye catching
• I prefer a Graphic to enhance the Volume No.
• Icons for
• 1. Questions and answers
• 2. Theory Notes
• 3. Tips & Tricks
• 4. Previous Year's Reference Questions
• 5. Covers Complete Syllabus
Nice to have
• decent seamless background or metallic 3d effect (not to be print in special Ink) design should only be in CMYK.
Should not have
• Physics related Pictures or Icons (Specially E=mc2) or any scientist photograph or I Need pure graphic design

```html
<!DOCTYPE html>
<html lang="en">
<head>
<meta charset="utf-8">
<title>Physics Volume 8 – Book Cover</title>
<link href="https://fonts.googleapis.com/css2?family=Oswald:wght@500&family=Poppins:wght@800&family=Archivo+Black&family=Montserrat:wght@400&display=swap" rel="stylesheet">
<style>
  :root {
    --canvas: #ffffff;
    --navy-deep: #020836;
    --navy: #0a1650;
    --navy-mid: #0d1d5c;
    --back-wall: #030a33;
    --silver-1: #5d7199;
    --silver-2: #d9e2f2;
    --silver-3: #7aa3d6;
    --teal: #2d6f92;
    --feature-text: #34437c;
    --logo-text: #a9bde0;
  }
  html, body {
    margin: 0;
    width: 1200px;
    height: 1200px;
    overflow: hidden;
    background: var(--canvas);
  }
  .cover {
    position: absolute;
    left: 322px;
    top: 211px;
    width: 555px;
    height: 778px;
    background: linear-gradient(180deg, var(--navy-mid) 0%, var(--navy) 40%, var(--navy-deep) 100%);
    overflow: hidden;
  }
  .cover__sky {
    position: absolute;
    left: 0; top: 0;
    width: 555px; height: 305px;
    background: radial-gradient(ellipse at 50% 100%, #1a2f7a 0%, #0e1c5e 45%, #0a1650 100%);
  }
  .cover__room {
    position: absolute;
    left: 0; top: 0;
  }
  .brand {
    position: absolute;
    left: 0; width: 555px;
    top: 46px;
    text-align: center;
    font-family: "Montserrat", sans-serif;
    font-weight: 400;
    font-size: 15px;
    letter-spacing: 2px;
    color: var(--logo-text);
  }
  .title {
    position: absolute;
    left: -222px;
    width: 1000px;
    top: 120px;
    margin: 0;
    text-align: center;
    white-space: nowrap;
    font-family: "Oswald", sans-serif;
    font-weight: 500;
    font-size: 150px;
    line-height: 1;
    letter-spacing: 30px;
    text-indent: 30px;
    transform: scaleX(0.56);
    transform-origin: 50% 50%;
  }
  .title__text {
    background: linear-gradient(90deg, var(--silver-1) 0%, var(--silver-2) 45%, var(--silver-3) 75%, var(--teal) 100%);
    -webkit-background-clip: text;
    background-clip: text;
    color: transparent;
  }
  .volume-number {
    position: absolute;
    left: 0; width: 555px;
    top: 388px;
    text-align: center;
    font-family: "Poppins", sans-serif;
    font-weight: 800;
    font-size: 160px;
    line-height: 1;
    background: linear-gradient(160deg, #bfd7ee 0%, #5fa5cf 40%, #e3eef8 60%, #2c93bf 100%);
    -webkit-background-clip: text;
    background-clip: text;
    color: transparent;
  }
  .volume-label {
    position: absolute;
    left: 0; width: 555px;
    top: 562px;
    text-align: center;
    font-family: "Archivo Black", sans-serif;
    font-size: 24px;
    letter-spacing: 2px;
    background: linear-gradient(90deg, #5c6e9a, #c4d0e6);
    -webkit-background-clip: text;
    background-clip: text;
    color: transparent;
  }
  .features {
    position: absolute;
    left: 0; width: 555px;
    top: 644px;
    margin: 0; padding: 0;
    list-style: none;
    text-align: center;
    font-family: "Montserrat", sans-serif;
    font-size: 17px;
    line-height: 22.5px;
    letter-spacing: 2px;
    color: var(--feature-text);
  }
</style>
</head>
<body>
  <div class="cover">
    <div class="cover__sky" role="img" aria-label="Perspective line grid pattern in blue over the title area"></div>
    <svg class="cover__room" width="555" height="778" viewBox="0 0 555 778" aria-hidden="true">
      <defs>
        <linearGradient id="leftWall" x1="0" x2="1">
          <stop offset="0" stop-color="#0c2a5e"/>
          <stop offset="1" stop-color="#061844"/>
        </linearGradient>
        <linearGradient id="rightWall" x1="1" x2="0">
          <stop offset="0" stop-color="#0c2a5e"/>
          <stop offset="1" stop-color="#061844"/>
        </linearGradient>
        <linearGradient id="ceiling" y1="0" y2="1">
          <stop offset="0" stop-color="#0a1f55"/>
          <stop offset="1" stop-color="#040d3a"/>
        </linearGradient>
        <linearGradient id="floor" y1="1" y2="0">
          <stop offset="0" stop-color="#0a1f55"/>
          <stop offset="1" stop-color="#030b36"/>
        </linearGradient>
      </defs>
      <polygon points="0,305 555,305 427,369 131,369" fill="url(#ceiling)"/>
      <polygon points="0,305 131,369 131,555 0,613" fill="url(#leftWall)"/>
      <polygon points="555,305 427,369 427,555 555,613" fill="url(#rightWall)"/>
      <polygon points="131,555 427,555 555,613 0,613" fill="url(#floor)"/>
      <rect x="131" y="369" width="296" height="186" fill="var(--back-wall)"/>
      <rect x="0" y="613" width="555" height="165" fill="#030a38" opacity="0.6"/>
      <line x1="0" y1="305" x2="555" y2="305" stroke="#1d3a7a" stroke-width="1"/>
    </svg>

    <div class="brand">VORLIN Education</div>
    <h1 class="title"><span class="title__text">PHYSICS</span></h1>
    <div class="volume-number">8</div>
    <div class="volume-label">VOLUME</div>
    <ul class="features">
      <li>questions and answers</li>
      <li>theory notes</li>
      <li>tips &amp; tricks</li>
      <li>previous year's reference questions</li>
      <li>covers complete syllabus</li>
    </ul>
  </div>
</body>
</html>
```